Etiketten-Design für eingekochte Erzeugnisse
Zielgruppe
Wir sind ein regional tätiger Cateringbetrieb und Hersteller von hausgemachten, qualitativ hochwertigen Saucen, Suppen und Dips. Für unsere eingekochten Erzeugnisse suchen wir ein Etikett für durchsichtige Gläser (327 ml, TO 66) mit kupferfarbenem Twist-Off-Deep Verschluss. Da es sich um hochwertige Produkte handelt, sollte dies auch das Etikett widerspiegeln und nicht „billig“ aussehen. Das Design sollte modern, hip und farblich zum Kupferdeckel passen.
Aufgabenstellung
Das Etikett sollte über den gesamten Umfang des Glases gehen. Als Endformat stellen wir uns eine Breite des Etiketts von 220 mm und eine Höhe von 90 mm vor.
Da wir unterschiedliche Sorten anbieten, sollten sich diese in den Etiketten wiederfinden. Jede Sorte sollte also ein individuell auf den Inhalt angepasstes Etikett haben. Zudem sollte das Etikett später auch anpassbar sein, da sich die Vorschriften zur Deklaration sowie die Zutatenliste ändern können. Die Grammangabe der Gesamtmenge sollte ebenfalls anpassbar sein können.
Für unsere Marke „Topfzauber“ suchen wir außerdem ein neues Wort-Bild-Logo,
welches gleich auf dem Etikett platziert werden soll. Das Logo sollte also in das Etikett eingefügt sein, aber auch für die Homepage und den Rechnungsbogen geeignet sein.
Unser Sortiment umfasst die Saucensorten:
- Tomatensauce
- Bratensauce
- Rahmsauce
- Bolognesesauce
- Chilli con Carne
- Linsenbolognese, vegetarisch
- Gelbes Thai Curry, vegetarisch
- Ungarische Gulaschsuppe
- Karibischer Süßkartoffel-Kürbis Eintopf
- Indischer Linsencurry
Was soll auf das Etikett:
Saucen Sorte (Bezeichnung)
Hersteller:
Partyservice Hellwanger
Markus Hellwanger
Lerchenfeld 9
88999 Beispielstadt
Inhalt:
360g
Zutaten:
Anpassbares Zutatentextfeld
Anpassbare Nährwerttabelle mit den Big 7
Haltbarkeit:
Mindestens haltbar bis: siehe Deckel
Hinweise:
Kann Spuren von Sellerie und Nüssen enthalten.
Kühl, trocken und lichtgeschützt lagern.
Nach dem Öffnen im Kühlschrank aufbewahren und innerhalb weniger Tage aufbrauchen.
Weiße Fläche freihalten, um später eventuell einen Barcode einzufügen.
Internetadresse:
www.topfzauber-beispiel.de

```html
<!DOCTYPE html>
<html lang="de">
<head>
<meta charset="utf-8">
<title>Topfzauber – Etiketten</title>
<link href="https://fonts.googleapis.com/css2?family=Amatic+SC:wght@700&family=Oswald:wght@300;400&display=swap" rel="stylesheet">
<style>
  :root {
    --bg: #ffffff;
    --tomato: #e0605c;
    --mushroom: #d3aa78;
    --chili: #8ab592;
    --chili-red: #d0282a;
    --badge: #1c1a19;
    --ink-light: #ffffff;
    --label-white: #f7f6f3;
  }
  * { margin: 0; padding: 0; box-sizing: border-box; }
  html, body { width: 1200px; height: 916px; overflow: hidden; background: var(--bg); }
  .canvas { position: relative; width: 1200px; height: 916px; }

  .label { position: absolute; top: 129px; width: 368px; height: 487px; }
  .label--tomato  { left: 18px;  --accent: var(--tomato); }
  .label--mushroom{ left: 421px; --accent: var(--mushroom); }
  .label--chili   { left: 818px; --accent: var(--chili); }

  .label__strap { position: absolute; left: 143px; top: 0; width: 62px; height: 212px; background: var(--accent); }
  .label__body { position: absolute; left: 0; top: 212px; width: 368px; height: 275px; background: var(--label-white); overflow: hidden; }
  .label__art { position: absolute; left: 0; top: 0; width: 300px; height: 275px; }
  .label__panel { position: absolute; left: 0; top: 0; width: 368px; height: 275px; }
  .label__panel path { fill: var(--accent); }

  .brand-badge {
    position: absolute; left: 117px; top: 148px; width: 106px; height: 106px;
    border-radius: 50%; background: var(--badge);
    display: flex; align-items: center; justify-content: center;
    font-family: "Amatic SC", cursive; font-weight: 700; font-size: 25px;
    color: var(--ink-light); letter-spacing: 0.5px; z-index: 2;
  }

  .label__text { position: absolute; left: 120px; top: 212px; width: 248px; height: 275px; text-align: center; color: var(--ink-light); z-index: 1; }
  .product-name { position: absolute; left: 0; right: 0; top: 54px; font-family: "Amatic SC", cursive; font-weight: 700; font-size: 44px; line-height: 1; letter-spacing: 0.5px; }
  .product-name--hot { color: var(--chili-red); font-size: 38px; top: 58px; }
  .product-claim { position: absolute; left: 0; right: 0; top: 100px; font-family: "Oswald", sans-serif; font-weight: 300; font-size: 14px; line-height: 21px; text-transform: uppercase; letter-spacing: 0.3px; }
  .product-claim--mixed { text-transform: none; font-size: 14.5px; letter-spacing: 0.5px; }
  .net-weight { position: absolute; left: 0; right: 0; top: 143px; font-family: "Oswald", sans-serif; font-weight: 300; line-height: 1; }
  .net-weight__caption { font-size: 10px; margin-right: 2px; }
  .net-weight__value { font-size: 26px; }
  .servings { position: absolute; left: 0; right: 0; top: 175px; font-family: "Oswald", sans-serif; font-weight: 300; font-size: 9.5px; }
</style>
</head>
<body>
<div class="canvas">

  <section class="label label--tomato">
    <div class="label__strap"></div>
    <div class="label__body">
      <svg class="label__art" role="img" aria-label="Aquarell-Illustration von Tomaten, Knoblauch und Pfefferkörnern" viewBox="0 0 300 275">
        <defs><linearGradient id="g-tomato" x1="0" y1="0" x2="1" y2="1"><stop offset="0" stop-color="#f1e9e4"/><stop offset="0.6" stop-color="#e79a8c"/><stop offset="1" stop-color="#d8564a"/></linearGradient></defs>
        <rect x="0" y="60" width="300" height="215" fill="url(#g-tomato)"/>
      </svg>
      <svg class="label__panel" viewBox="0 0 368 275"><path d="M94 0 C98 140 190 245 300 275 L368 275 L368 0 Z"/></svg>
    </div>
    <div class="brand-badge">Topfzauber</div>
    <div class="label__text">
      <h2 class="product-name">Tomatensauce</h2>
      <p class="product-claim">Vollreife aromatische Tomaten<br>und mediterrane Gewürze</p>
      <p class="net-weight"><span class="net-weight__caption">Inhalt</span><span class="net-weight__value">360g</span></p>
      <p class="servings">Ergibt 2 Portionen</p>
    </div>
  </section>

  <section class="label label--mushroom">
    <div class="label__strap"></div>
    <div class="label__body">
      <svg class="label__art" role="img" aria-label="Aquarell-Illustration von Steinpilzen mit Beeren und Kräutern" viewBox="0 0 300 275">
        <defs><linearGradient id="g-mushroom" x1="0" y1="0" x2="1" y2="1"><stop offset="0" stop-color="#efebe4"/><stop offset="0.55" stop-color="#c9b49a"/><stop offset="1" stop-color="#8f9a6e"/></linearGradient></defs>
        <rect x="0" y="70" width="300" height="205" fill="url(#g-mushroom)"/>
      </svg>
      <svg class="label__panel" viewBox="0 0 368 275"><path d="M94 0 C98 140 190 245 300 275 L368 275 L368 0 Z"/></svg>
    </div>
    <div class="brand-badge">Topfzauber</div>
    <div class="label__text">
      <h2 class="product-name">Pilzrahmsauce</h2>
      <p class="product-claim">Verschiedene Edelpilze<br>und frische Sahne</p>
      <p class="net-weight"><span class="net-weight__caption">Inhalt</span><span class="net-weight__value">360g</span></p>
      <p class="servings">Ergibt 2 Portionen</p>
    </div>
  </section>

  <section class="label label--chili">
    <div class="label__strap"></div>
    <div class="label__body">
      <svg class="label__art" role="img" aria-label="Aquarell-Illustration von roten und grünen Chilischoten" viewBox="0 0 300 275">
        <defs><linearGradient id="g-chili" x1="0" y1="0" x2="1" y2="1"><stop offset="0" stop-color="#eef1ea"/><stop offset="0.5" stop-color="#8fb08a"/><stop offset="1" stop-color="#d2453a"/></linearGradient></defs>
        <rect x="0" y="20" width="300" height="255" fill="url(#g-chili)"/>
      </svg>
      <svg class="label__panel" viewBox="0 0 368 275"><path d="M94 0 C98 140 190 245 300 275 L368 275 L368 0 Z"/></svg>
    </div>
    <div class="brand-badge">Topfzauber</div>
    <div class="label__text">
      <h2 class="product-name product-name--hot">Chili con Carne</h2>
      <p class="product-claim product-claim--mixed">Kidney-Beans · Rindfleisch<br>und extra scharfes Chili</p>
      <p class="net-weight"><span class="net-weight__caption">Inhalt</span><span class="net-weight__value">360g</span></p>
      <p class="servings">Ergibt 2 Portionen</p>
    </div>
  </section>

</div>
</body>
</html>
```